Tall Oak Circle.. a non profit that seeks to stomp out skin cancer .. smalls steps toward making big

Simple letterhead incorporating logo

Industry/Entity Type

Non Profit

Font styles to use
Sans Serif

Colors

Designer to choose colors to be used in the design.

```html
<!DOCTYPE html>
<html lang="en">
<head>
<meta charset="utf-8">
<title>Tall Oak Circle — Letterhead</title>
<link rel="stylesheet" href="https://fonts.googleapis.com/css2?family=Lato:wght@300;400&display=swap">
<style>
  :root {
    --backdrop: #e9e9ea;
    --paper: #ffffff;
    --navy: #1f294a;
    --sun: #f2e01c;
  }
  * { box-sizing: border-box; margin: 0; padding: 0; }
  html, body {
    width: 1200px;
    height: 1000px;
    overflow: hidden;
    background: var(--backdrop);
    font-family: "Lato", sans-serif;
  }
  .letterhead {
    position: absolute;
    left: 280px;
    top: 70px;
    width: 640px;
    height: 860px;
    background: var(--paper);
    box-shadow: 0 2px 10px rgba(0,0,0,0.08);
  }
  .header-band {
    position: absolute;
    left: 26px;
    right: 26px;
    top: 44px;
    height: 15px;
    background: var(--navy);
  }
  .brand {
    position: absolute;
    left: 50%;
    top: 51px;
    transform: translate(-50%, -50%);
    display: flex;
    align-items: center;
    gap: 10px;
    padding: 0 16px;
    height: 40px;
    background: var(--paper);
    white-space: nowrap;
  }
  .brand-dot {
    width: 12px;
    height: 12px;
    border-radius: 50%;
    background: var(--sun);
    flex: none;
  }
  .brand-name {
    color: var(--navy);
    font-weight: 300;
    font-size: 22px;
    line-height: 1;
    letter-spacing: 0.3px;
  }
  .footer-band {
    position: absolute;
    left: 26px;
    right: 26px;
    bottom: 40px;
    height: 18px;
    background: var(--navy);
    display: flex;
    align-items: center;
    padding-left: 82px;
    gap: 48px;
  }
  .contact-item {
    display: flex;
    align-items: center;
    gap: 5px;
    color: var(--sun);
    font-size: 9.5px;
    font-weight: 400;
    letter-spacing: 0.2px;
    white-space: nowrap;
  }
  .contact-item svg { width: 9px; height: 9px; flex: none; }
</style>
</head>
<body>
  <main class="letterhead">
    <div class="header-band"></div>
    <div class="brand">
      <span class="brand-dot" aria-hidden="true"></span>
      <span class="brand-name">Tall Oak Circle</span>
    </div>

    <footer class="footer-band">
      <span class="contact-item">
        <svg viewBox="0 0 10 10" aria-hidden="true"><rect x="2.5" y="0.5" width="5" height="9" rx="1" fill="none" stroke="#f2e01c" stroke-width="1"/><circle cx="5" cy="8" r="0.6" fill="#f2e01c"/></svg>
        +123 5550147
      </span>
      <span class="contact-item">
        <svg viewBox="0 0 10 10" aria-hidden="true"><rect x="0.5" y="2" width="9" height="6" fill="#f2e01c"/><path d="M0.5 2 L5 5.5 L9.5 2" fill="none" stroke="#1f294a" stroke-width="0.9"/></svg>
        hello@talloakcircle.org
      </span>
      <span class="contact-item">
        <svg viewBox="0 0 10 10" aria-hidden="true"><circle cx="5" cy="5" r="4.3" fill="none" stroke="#f2e01c" stroke-width="1"/><ellipse cx="5" cy="5" rx="1.8" ry="4.3" fill="none" stroke="#f2e01c" stroke-width="0.8"/><line x1="0.7" y1="5" x2="9.3" y2="5" stroke="#f2e01c" stroke-width="0.8"/></svg>
        www.talloakcircle.org
      </span>
    </footer>
  </main>
</body>
</html>
```